Lets get creative with Pelloway Finance Brochure

I have used artfolkhub before for a previous brochure which is attached business BRAMLE Automotive. I would like to work together on a new project PELLOWAY Finance. https://pellowayfinance.com.au/
It is a boutique Finance company ideally targeting the small to Medium business s along with consumer finance. I have attached previous brochure to give an idea of layout. Once we have a layout i will send wording through.

Target Market(s)

business owners

Industry/Entity Type

Finance

Font styles to use
Serif

Colors
0355a3
fef3ec

```html
<!DOCTYPE html>
<html lang="en">
<head>
<meta charset="utf-8">
<title>Pelloway Finance – Trifold Brochure</title>
<link rel="stylesheet" href="https://fonts.googleapis.com/css2?family=Lora:ital,wght@0,400;0,500;0,700;1,700&family=Playfair+Display:ital,wght@0,700;1,700&display=swap">
<style>
  :root{
    --blue:#0355a3;
    --blue-deep:#023f7a;
    --blue-soft:#4a86c2;
    --cream:#fef3ec;
    --slate:#1f2c3d;
    --ink:#22272e;
    --backdrop:#b9bbbd;
  }
  *{box-sizing:border-box;margin:0;padding:0}
  html,body{width:848px;height:1200px;overflow:hidden}
  body{background:var(--backdrop);font-family:"Lora",serif;color:var(--ink);position:relative}

  .spread{position:absolute;left:44px;width:759px;height:537px;display:flex;box-shadow:0 6px 18px rgba(0,0,0,.25)}
  .spread--outside{top:40px}
  .spread--inside{top:623px}

  .panel{position:relative;width:253px;height:537px;overflow:hidden}
  .panel + .panel{border-left:1px solid rgba(0,0,0,.08)}
  .panel__shapes{position:absolute;inset:0;width:253px;height:537px}
  .panel--dark{background:var(--slate);color:var(--cream)}
  .panel--light{background:var(--cream)}

  .hexagon{position:absolute;width:20px;height:22px}
  .heading{position:absolute;font-family:"Playfair Display",serif;font-weight:700;line-height:1.12}
  .heading--blue{color:var(--blue)}
  .heading--cream{color:var(--cream)}

  .bullets{list-style:disc;padding-left:12px;font-size:7.5px;line-height:1.5}
  .body-copy{font-size:7.5px;line-height:1.5}

  .brand{position:absolute;left:0;right:0;display:flex;align-items:center;justify-content:center;gap:7px;
         font-family:"Lora",serif;font-weight:700;font-size:17px;letter-spacing:.3px;color:var(--blue)}
  .brand__mark{width:9px;height:9px;background:var(--blue)}

  .website{position:absolute;font-family:"Lora",serif;font-weight:700;color:var(--cream)}

  /* outside: back panel */
  .back .hexagon{left:14px;top:56px}
  .back .heading{left:42px;top:52px;font-size:19px;font-style:italic;color:var(--cream)}
  .back .bullets{position:absolute;left:34px;top:168px;width:190px;color:var(--cream)}
  .back .website{left:18px;bottom:30px;font-size:16px}

  /* outside: contact panel */
  .contact__title{position:absolute;left:0;right:0;top:74px;text-align:center;font-family:"Playfair Display",serif;font-weight:700;font-size:14px;color:var(--blue-deep)}
  .contact__block{position:absolute;left:0;right:0;text-align:center;font-size:7.5px;line-height:1.5}
  .contact__block strong{font-weight:700;display:block}
  .contact__hours{top:108px}
  .contact__address{top:160px}
  .contact .brand{top:318px}

  /* outside: cover */
  .cover__headline{position:absolute;left:44px;top:82px;width:190px;font-family:"Playfair Display",serif;font-weight:700;font-size:17px;line-height:1.25;color:#fff}
  .cover .hexagon{left:14px;top:86px}
  .cover .brand{top:429px;font-size:19px}

  /* inside: about */
  .about .hexagon{left:16px;top:80px}
  .about .heading{left:44px;top:76px;font-size:15px}
  .about__section{position:absolute;left:30px;width:200px}
  .about__section h3{font-family:"Playfair Display",serif;font-size:10px;font-weight:700;margin-bottom:4px;color:var(--blue-deep)}
  .about__us{top:140px}
  .about__why{top:268px}

  /* inside: feature */
  .feature .brand{top:298px}

  /* inside: services */
  .services .hexagon{left:14px;top:58px}
  .services .heading{left:42px;top:52px;font-size:15px}
  .service{position:absolute;left:30px;width:200px;color:var(--cream)}
  .service h3{font-family:"Playfair Display",serif;font-size:9px;font-weight:700;margin-bottom:3px;color:#9cc3ea}
  .service--a{top:120px}
  .service--b{top:220px}
  .service--c{top:320px}
  .services .website{left:22px;bottom:40px;font-size:16px}
  .services .hexagon--corner{left:auto;top:auto;right:10px;bottom:38px}
</style>
</head>
<body>

<section class="spread spread--outside">

  <article class="panel panel--dark back">
    <svg class="hexagon" viewBox="0 0 20 22"><polygon points="10,0 20,5.5 20,16.5 10,22 0,16.5 0,5.5" fill="var(--blue-soft)"/></svg>
    <h2 class="heading">Your<br>Boutique<br>Finance<br>Company</h2>
    <ul class="bullets">
      <li>Lorem ipsum dolor sit amet,</li>
      <li>consectetur adipiscing elit, sed</li>
      <li>do eiusmod tempor incididunt ut</li>
      <li>labore et dolore magna aliqua</li>
      <li>Ut enim ad minim veniam, quis</li>
      <li>nostrud exercitation ullamco</li>
      <li>laboris nisi ut aliquip ex ea come</li>
      <li>Ut enim ad minim veniam, quis</li>
      <li>nostrud exercitation ullamco</li>
      <li>laboris nisi ut aliquip ex ea come</li>
    </ul>
    <p class="website">pellowayfinance.com.au</p>
  </article>

  <article class="panel panel--light contact">
    <svg class="panel__shapes" viewBox="0 0 253 537">
      <defs>
        <linearGradient id="towerHaze" x1="0" y1="0" x2="0" y2="1">
          <stop offset="0" stop-color="#fef3ec"/>
          <stop offset="1" stop-color="#e6e4e2"/>
        </linearGradient>
      </defs>
      <rect x="0" y="0" width="253" height="537" fill="url(#towerHaze)" role="img" aria-label="Faded photograph of a glass office tower"/>
      <path d="M0 0H253V44Q130 62 0 50Z" fill="var(--blue)"/>
      <rect x="0" y="300" width="253" height="56" fill="var(--cream)" opacity=".95"/>
      <path d="M0 478Q120 460 253 470V537H0Z" fill="var(--blue-soft)"/>
    </svg>
    <h2 class="contact__title">PELLOWAY FINANCE</h2>
    <p class="contact__block contact__hours"><strong>HOURS OF OPERATION</strong>MON-FRI: 8:30AM - 5:30PM<br>SAT: 8:30AM - 12NOON</p>
    <p class="contact__block contact__address"><strong>ADDRESS</strong>18 Harlow Lane<br>Email<br>Phone no<br>07 3000 1846</p>
    <div class="brand"><span class="brand__mark"></span>Pelloway Finance</div>
  </article>

  <article class="panel cover">
    <svg class="panel__shapes" viewBox="0 0 253 537">
      <defs>
        <linearGradient id="skyTowers" x1="0" y1="0" x2="1" y2="1">
          <stop offset="0" stop-color="#3f7fb8"/>
          <stop offset=".45" stop-color="#e9edf1"/>
          <stop offset="1" stop-color="#4d5e6e"/>
        </linearGradient>
      </defs>
      <rect x="0" y="0" width="253" height="537" fill="url(#skyTowers)" role="img" aria-label="Photograph looking up at glass skyscrapers against a cloudy sky"/>
      <path d="M0 0H253V36Q130 22 0 40Z" fill="var(--blue)"/>
      <rect x="0" y="408" width="253" height="62" fill="var(--cream)"/>
    </svg>
    <svg class="hexagon" viewBox="0 0 20 22"><polygon points="10,0 20,5.5 20,16.5 10,22 0,16.5 0,5.5" fill="var(--blue)"/></svg>
    <h1 class="cover__headline">We Finance your Company to bring the Change</h1>
    <div class="brand"><span class="brand__mark"></span>Pelloway Finance</div>
  </article>

</section>

<section class="spread spread--inside">

  <article class="panel panel--light about">
    <svg class="panel__shapes" viewBox="0 0 253 537">
      <path d="M0 0H253V40Q120 30 0 58Z" fill="var(--blue)"/>
      <path d="M0 486Q130 462 253 462V537H0Z" fill="var(--blue-soft)"/>
    </svg>
    <svg class="hexagon" viewBox="0 0 20 22"><polygon points="10,0 20,5.5 20,16.5 10,22 0,16.5 0,5.5" fill="var(--blue)"/></svg>
    <h2 class="heading heading--blue">Your Boutique<br>Finance Company</h2>
    <div class="about__section about__us">
      <h3>ABOUT US</h3>
      <p class="body-copy">Lorem ipsum dolor sit amet, consectetur adipiscing elit, sed do eiusmod tempor incididunt ut labore et dolore magna aliqua. Ut enim ad minim veniam, quis nostrud exercitation ullamco laboris nisi ut aliquip ex ea commodo consequat. Duis aute irure dolor</p>
    </div>
    <div class="about__section about__why">
      <h3>WHY CHOOSE US?</h3>
      <ul class="bullets">
        <li>Lorem ipsum dolor sit amet,</li>
        <li>consectetur adipiscing elit, sed</li>
        <li>do eiusmod tempor incididunt ut</li>
        <li>labore et dolore magna aliqua.</li>
        <li>Ut enim ad minim veniam, quis</li>
        <li>nostrud exercitation ullamco</li>
        <li>laboris nisi ut aliquip ex ea come</li>
      </ul>
    </div>
  </article>

  <article class="panel feature">
    <svg class="panel__shapes" viewBox="0 0 253 537">
      <defs>
        <linearGradient id="cityGrey" x1="0" y1="0" x2="1" y2="1">
          <stop offset="0" stop-color="#8d9094"/>
          <stop offset=".5" stop-color="#cfcfcf"/>
          <stop offset="1" stop-color="#55595e"/>
        </linearGradient>
      </defs>
      <rect x="0" y="0" width="253" height="537" fill="url(#cityGrey)" role="img" aria-label="Black and white aerial photograph of city towers"/>
      <path d="M0 0H253V26Q130 20 0 32Z" fill="var(--blue)"/>
      <rect x="0" y="280" width="253" height="60" fill="var(--cream)" opacity=".96"/>
      <path d="M0 462Q130 446 253 436V537H0Z" fill="var(--blue-soft)" opacity=".92"/>
    </svg>
    <div class="brand"><span class="brand__mark"></span>Pelloway Finance</div>
  </article>

  <article class="panel panel--dark services">
    <svg class="hexagon" viewBox="0 0 20 22"><polygon points="10,0 20,5.5 20,16.5 10,22 0,16.5 0,5.5" fill="var(--blue-soft)"/></svg>
    <h2 class="heading heading--cream">Your Boutique<br>Finance Company</h2>
    <div class="service service--a">
      <h3>A.</h3>
      <p class="body-copy">Lorem ipsum dolor sit amet, consectetur adipiscing elit, sed do eiusmod tempor incididunt ut labore et dolore magna aliqua. Ut enim ad minim veniam, quis nostrud</p>
    </div>
    <div class="service service--b">
      <h3>B.</h3>
      <p class="body-copy">Lorem ipsum dolor sit amet, consectetur adipiscing elit, sed do eiusmod tempor incididunt ut labore et dolore magna aliqua. Ut enim ad minim veniam, quis nostrud</p>
    </div>
    <div class="service service--c">
      <h3>C.</h3>
      <p class="body-copy">Lorem ipsum dolor sit amet, consectetur adipiscing elit, sed do eiusmod tempor incididunt ut labore et dolore magna aliqua. Ut enim ad minim veniam, quis nostrud</p>
    </div>
    <p class="website">pellowayfinance.com.au</p>
    <svg class="hexagon hexagon--corner" viewBox="0 0 20 22"><polygon points="10,0 20,5.5 20,16.5 10,22 0,16.5 0,5.5" fill="var(--blue-soft)"/></svg>
  </article>

</section>

</body>
</html>
```